Web Design for One for One Organic Soap Company

We need a website design for the company Tidewell Botanics based on the package design per attached.

The design should communicate high end, luxury organic. The site will provide facts about how the spread of disease causes deaths and can be prevented with hand washing. The site will also have a page about why we are passionate about organics and how that relates to our skin including skin facts.
Also, the site should have an e-commerce product page and shopping cart.

Target Market(s)

Educated, health conscious and socially conscious consumers who shop luxury. Target vendors include Larkmont Grocers and Velbrook..

Industry/Entity Type

E-Commerce

Font styles to use
Other font styles liked:
• See attached

Requirements
Must have
• Use of Ying Yang leaf Logo provided.
Based on design provided.

```html
<!DOCTYPE html>
<html lang="en">
<head>
<meta charset="utf-8">
<title>Tidewell Botanics — Organic Soap</title>
<link href="https://fonts.googleapis.com/css2?family=Open+Sans:ital,wght@0,400;0,600;1,600&display=swap" rel="stylesheet">
<style>
:root{
  --page-bg:#a98f6f;
  --tan:#cdb08e;
  --tan-light:#e3cfb6;
  --brown-dark:#3a2717;
  --brown:#5c4028;
  --text:#3d2b1c;
  --muted:#4a4a4a;
  --accent-red:#c0392b;
  --white:#ffffff;
}
*{margin:0;padding:0;box-sizing:border-box}
html,body{width:1093px;height:1200px;overflow:hidden}
body{background:var(--page-bg);font-family:"Open Sans",sans-serif;color:var(--text);position:relative}
.site{position:absolute;left:143px;top:43px;width:802px;height:1157px;background:var(--white);border-radius:16px 16px 0 0;overflow:hidden;box-shadow:0 0 30px rgba(40,25,10,.45)}
.header{position:absolute;left:0;top:0;width:802px;height:107px;background:var(--tan)}
.brand{position:absolute;left:32px;top:27px;display:flex;align-items:center;gap:10px}
.brand-mark{width:42px;height:42px;background:var(--accent-red)}
.brand-name{font-size:22px;font-weight:400;color:var(--brown-dark)}
.account{position:absolute;right:25px;top:22px;font-size:12.5px;color:var(--brown-dark)}
.account .login{color:var(--accent-red)}
.account .sep{margin:0 8px}
.nav{position:absolute;left:318px;top:66px;display:flex;font-size:12.5px}
.nav a{color:var(--brown-dark);text-decoration:none;padding:0 12px;line-height:26px;height:26px}
.nav a.active{background:var(--brown);color:var(--white);padding:0 14px}
.search{position:absolute;left:619px;top:66px;width:158px;height:26px;background:#f4f0ea;display:flex;align-items:center;justify-content:space-between;padding:0 8px;font-size:11.5px;color:#555}
.hero{position:absolute;left:31px;top:114px;width:747px;height:367px;border:5px solid var(--tan);border-radius:3px;background:linear-gradient(100deg,#e4e4e6 0%,#cfd0d3 45%,#e6b8a3 70%,#dcdcde 100%)}
.dots{position:absolute;left:348px;top:494px;width:99px;height:26px;border-radius:13px;background:#fafafa;box-shadow:0 2px 4px rgba(0,0,0,.25);display:flex;align-items:center;justify-content:center;gap:8px}
.dots span{width:12px;height:12px;border-radius:50%;border:1px solid #bbb;background:#fff}
.dots span.on{background:var(--tan);border-color:#b8956c}
.section-title{position:absolute;left:0;width:802px;text-align:center;font-size:16px;font-weight:600;color:var(--brown-dark);text-decoration:underline;text-underline-offset:3px}
.products{position:absolute;left:31px;top:596px;width:746px;height:209px;background:var(--tan);border-radius:6px}
.product{position:absolute;top:31px;width:187px;text-align:center}
.product .thumb{width:187px;height:120px;border:4px solid var(--tan-light)}
.product .name{margin-top:14px;font-size:15px;color:var(--brown-dark)}
.arrow{position:absolute;top:75px}
.why-text{position:absolute;left:100px;top:894px;width:602px;text-align:center;font-size:11.5px;line-height:19px;color:var(--muted)}
.btn{position:absolute;left:351px;top:983px;width:91px;height:32px;background:var(--brown);color:var(--white);font-size:11.5px;font-weight:600;font-style:italic;display:flex;align-items:center;justify-content:center}
.footer{position:absolute;left:0;top:1069px;width:802px;height:88px;background:var(--brown-dark);border-top:3px solid #5a4330;text-align:center;color:#cdb79c;font-size:11px}
.footer-links{margin-top:20px}
.footer-links a{color:#cdb79c;text-decoration:none}
.footer-links a.active{color:var(--white)}
.footer-links .sep{margin:0 11px}
.copyright{margin-top:8px}
</style>
</head>
<body>
<div class="site">
  <header class="header">
    <div class="brand"><div class="brand-mark"></div><div class="brand-name">Tidewell Botanics</div></div>
    <div class="account"><span class="login">Login</span><span class="sep">|</span>Register<span class="sep">|</span>Shopping Cart :&nbsp; 0</div>
    <nav class="nav"><a class="active" href="#">Home</a><a href="#">About Us</a><a href="#">Products</a><a href="#">Contacts</a></nav>
    <div class="search">Search here
      <svg width="15" height="15" viewBox="0 0 15 15"><circle cx="6" cy="6" r="4.5" fill="none" stroke="#6b8aa8" stroke-width="1.5"/><line x1="9.3" y1="9.3" x2="13.5" y2="13.5" stroke="#6b8aa8" stroke-width="2"/></svg>
    </div>
  </header>

  <div class="hero" role="img" aria-label="Soap box beside running water and lathered hands"></div>
  <div class="dots"><span class="on"></span><span></span><span></span><span></span></div>

  <h2 class="section-title" style="top:561px">Our Products</h2>
  <section class="products">
    <svg class="arrow" style="left:18px" width="16" height="30" viewBox="0 0 16 30"><polyline points="13,3 3,15 13,27" fill="none" stroke="#fff" stroke-width="2.5"/></svg>
    <div class="product" style="left:62px"><div class="thumb" role="img" aria-label="Lavender soap bars" style="background:linear-gradient(160deg,#8a8494,#5f5968)"></div><div class="name">Lavender Soap</div></div>
    <div class="product" style="left:282px"><div class="thumb" role="img" aria-label="Lemongrass tea soap bars" style="background:linear-gradient(160deg,#ddd27a,#c9bf5a)"></div><div class="name">Emongrasstea Soap</div></div>
    <div class="product" style="left:499px"><div class="thumb" role="img" aria-label="Clove soap bars" style="background:linear-gradient(180deg,#7a5440 0%,#8e6548 55%,#e39d6e 75%,#c67a4c 100%)"></div><div class="name">Soapclove</div></div>
    <svg class="arrow" style="left:712px" width="16" height="30" viewBox="0 0 16 30"><polyline points="3,3 13,15 3,27" fill="none" stroke="#fff" stroke-width="2.5"/></svg>
  </section>

  <h2 class="section-title" style="top:859px">Whu you should use organic Soap</h2>
  <p class="why-text">The site will provide facts about how the spread of disease causes deaths and can be prevented with hand washing. The site will also have a page about why we are passionate about organics and<br>how that relates to our skin including skin facts.</p>
  <a class="btn">Know More</a>

  <footer class="footer">
    <div class="footer-links"><a class="active" href="#">Home</a><span class="sep">|</span><a href="#">About Us</a><span class="sep">|</span><a href="#">Products</a><span class="sep">|</span><a href="#">Contacts</a><span class="sep">|</span><a href="#">Privacy Policy</a></div>
    <div class="copyright">Copyright@2014, Tidewell Botanics</div>
  </footer>
</div>
</body>
</html>
```